We're a trash valet service. We collect trash that tenants at apartment communitys, elder/assisted liveing would be ideal but we collect Sunday through Thursdays and also offer morning check ups to make sure nothing is left out for pickup. Id like it basic but elegant with little to no cartoon caricatures. But not aposed to them if done right. Colors tequise, orange, blue not married to any of the in spasific.

Lanternway Hauling
Number : 555-314-7290
Address: 438 Quarry Ridge Road SUITE
Millbrook NJ 08000
Email: Marla@lanternway-hauling.example

I attached my logo.
Those don't have to be the colors plain black is fine for the broshour but I do like those colors with orange maybe.
Updates

Everyone is doing such amazing work. I wanted to just make sure I let everyone know what I need and what should not be on broshour. We do not have garbage trucks, we just both of trash in on site dumpsters or compactors. We use tall kitchen cans for residents to put their garbage in and on in the cans outside of their doors. Pictures of hallways with cans with our logo on it would be good definitely no one's face. What we provide for managers and their benefiting from our service. residents expierance. We also don't have a QR code scanner. And the morning check up is an added service.

Target Market(s)

Apartment communitys

Requirements
Should not have
• Garbage trucks

```html
<!DOCTYPE html>
<html lang="en">
<head>
<meta charset="utf-8">
<title>Lanternway Hauling – Valet Trash Brochure</title>
<link href="https://fonts.googleapis.com/css2?family=Poppins:wght@400;500;600;700;800&display=swap" rel="stylesheet">
<style>
  :root{
    --navy:#22365a;
    --navy-text:#1f3350;
    --orange:#d4804a;
    --orange-soft:#dba170;
    --sky:#dbe6f1;
    --sky-deep:#b9d0e6;
    --shadow:#d0d0d0;
    --white:#ffffff;
    --ink:#111827;
  }
  *{box-sizing:border-box;margin:0;padding:0}
  html,body{width:1200px;height:769px;overflow:hidden;background:var(--white)}
  body{position:relative;font-family:'Poppins',sans-serif;color:var(--ink)}

  .page-shadow{position:absolute;width:395px;height:510px;background:var(--shadow);filter:blur(2px)}
  .page{position:absolute;top:124px;width:395px;height:510px;background:var(--white);overflow:hidden}
  .page--cover{left:173px}
  .page--services{left:610px}
  .page-shadow--cover{left:211px;top:162px}
  .page-shadow--services{left:648px;top:162px}

  /* cover */
  .cover-shape{position:absolute;left:0;top:0}
  .hero-photo{position:absolute;left:14px;top:84px;width:216px;height:216px;border-radius:50%;
    background:radial-gradient(circle at 55% 55%,#2b2d31 0 30%,#6b6f66 31% 45%,#b8bcc0 60%,#d9dcde 100%)}
  .sky-circles{position:absolute;right:-81px;top:159px;width:162px;height:162px;border-radius:50%;background:var(--sky)}
  .sky-circles::after{content:"";position:absolute;left:29px;top:29px;width:104px;height:104px;border-radius:50%;background:var(--sky-deep)}

  .brand{position:absolute;display:flex;flex-direction:column;align-items:center;color:var(--navy-text);font-weight:800;text-transform:uppercase;text-align:center}
  .brand-mark{background:var(--navy);}
  .brand--cover{right:26px;top:24px;gap:8px}
  .brand--cover .brand-mark{width:62px;height:62px}
  .brand--cover .brand-name{font-size:17px;line-height:1.05;letter-spacing:.3px}
  .brand--services{right:17px;top:24px;gap:4px}
  .brand--services .brand-mark{width:30px;height:30px}
  .brand--services .brand-name{font-size:8px;line-height:1.05}

  .cover-headline{position:absolute;top:330px;left:0;width:100%;text-align:center;font-weight:800;font-size:23px;line-height:1.22;color:var(--navy-text);letter-spacing:-.2px}
  .cover-headline .accent{color:var(--orange)}

  /* footer */
  .contact-bar{position:absolute;left:0;bottom:0;width:100%;height:110px;background:var(--navy);color:var(--orange)}
  .contact-phone{position:absolute;top:16px;left:0;width:100%;display:flex;justify-content:center;align-items:center;gap:12px;font-weight:800;font-size:32px;letter-spacing:.5px}
  .contact-details{position:absolute;top:70px;left:18px;right:14px;display:flex;justify-content:space-between;align-items:center;font-weight:700;font-size:8.3px;line-height:1.35}
  .contact-item{display:flex;align-items:center;gap:8px}

  /* services */
  .services-title{position:absolute;left:28px;top:30px;font-weight:800;font-size:23px;color:var(--navy-text)}
  .service-list{position:absolute;left:28px;top:80px;width:350px;list-style:none;display:flex;flex-direction:column;gap:15px}
  .service{display:flex;gap:10px;align-items:flex-start}
  .service-art{flex:none;width:51px;height:43px;border-radius:4px;background:linear-gradient(135deg,#cfe3ee,#7fb0c9)}
  .service-name{font-weight:500;font-size:12.2px;color:var(--ink);line-height:1.25}
  .service-text{font-weight:500;font-size:9.6px;line-height:1.45;color:var(--ink)}

  .tagline-band{position:absolute;left:0;top:258px;width:100%;height:60px;background:var(--orange);color:var(--white);display:flex;align-items:center;justify-content:center;text-align:center;font-weight:800;font-size:17.6px;line-height:1.2}
  .process{position:absolute;top:346px;left:0;width:100%;display:flex;justify-content:center;align-items:center;gap:8px;font-weight:800;font-size:17px;color:var(--navy-text)}
  .process-arrow{width:0;height:0;border-top:7px solid transparent;border-bottom:7px solid transparent;border-left:12px solid var(--orange)}
</style>
</head>
<body>

<div class="page-shadow page-shadow--cover"></div>
<div class="page-shadow page-shadow--services"></div>

<!-- Cover page -->
<section class="page page--cover">
  <svg class="cover-shape" width="395" height="330" viewBox="0 0 395 330">
    <path d="M0 0 H145 L215 100 Q258 165 250 205 A128 128 0 0 1 0 250 Z" fill="var(--orange)"/>
    <circle cx="77" cy="17" r="54" fill="none" stroke="var(--orange-soft)" stroke-width="1"/>
    <circle cx="77" cy="17" r="38" fill="var(--orange-soft)"/>
  </svg>
  <div class="hero-photo" role="img" aria-label="Gloved hand carrying a tied black trash bag outside an apartment building"></div>
  <div class="sky-circles"></div>

  <div class="brand brand--cover">
    <span class="brand-mark"></span>
    <span class="brand-name">Lanternway<br>Hauling</span>
  </div>

  <h1 class="cover-headline">Seamless Doorstep Collection<br>&amp; <span class="accent">Morning Peace of Mind</span></h1>

  <footer class="contact-bar">
    <div class="contact-phone">
      <svg width="32" height="32" viewBox="0 0 24 24" fill="var(--white)"><path d="M6.6 10.8a15.1 15.1 0 0 0 6.6 6.6l2.2-2.2a1 1 0 0 1 1-.25 11.4 11.4 0 0 0 3.6.57 1 1 0 0 1 1 1V20a1 1 0 0 1-1 1A17 17 0 0 1 3 4a1 1 0 0 1 1-1h3.5a1 1 0 0 1 1 1c0 1.25.2 2.45.57 3.57a1 1 0 0 1-.25 1z"/><path d="M15 3a6 6 0 0 1 6 6M15 6a3 3 0 0 1 3 3" stroke="var(--white)" stroke-width="1.6" fill="none" stroke-linecap="round"/></svg>
      <span>555-314-7290</span>
    </div>
    <div class="contact-details">
      <div class="contact-item">
        <svg width="16" height="19" viewBox="0 0 16 20"><path d="M8 0a8 8 0 0 0-8 8c0 6 8 12 8 12s8-6 8-12a8 8 0 0 0-8-8z" fill="var(--white)"/><circle cx="8" cy="8" r="3" fill="var(--navy)"/></svg>
        <span>438 Quarry Ridge Road SUITE<br>Millbrook NJ 08000</span>
      </div>
      <div class="contact-item">
        <svg width="16" height="13" viewBox="0 0 16 13"><rect x=".75" y=".75" width="14.5" height="11.5" fill="none" stroke="var(--white)" stroke-width="1.5"/><path d="M1 1l14 11M15 1L1 12" stroke="var(--white)" stroke-width="1.3"/></svg>
        <span>Marla@lanternway-hauling.example</span>
      </div>
    </div>
  </footer>
</section>

<!-- Services page -->
<section class="page page--services">
  <h2 class="services-title">Our Core Services</h2>
  <div class="brand brand--services">
    <span class="brand-mark"></span>
    <span class="brand-name">Lanternway<br>Hauling</span>
  </div>

  <ul class="service-list">
    <li class="service">
      <div class="service-art" role="img" aria-label="Calendar showing Sunday to Thursday pickups beside a trash bag"></div>
      <div>
        <h3 class="service-name">5-Night Weekly Collection</h3>
        <p class="service-text">Reliable pickup Sunday through Thursday evenings.<br>keeping waste off the property during peak hours.</p>
      </div>
    </li>
    <li class="service">
      <div class="service-art" role="img" aria-label="Clock and magnifying glass over an apartment doorway"></div>
      <div>
        <h3 class="service-name">Morning Compliance Audits</h3>
        <p class="service-text">Our team performs morning check-ups to make sure<br>no trash bags or loose items are left behind at doorsteps.</p>
      </div>
    </li>
    <li class="service">
      <div class="service-art" role="img" aria-label="Apartment buildings and a small residence"></div>
      <div>
        <h3 class="service-name">Tailored Property Solutions</h3>
        <p class="service-text">Designed specifically for multi-family apartment<br>communities and senior/assisted living facilities.</p>
      </div>
    </li>
  </ul>

  <div class="tagline-band">Reliable Doorstep Valet Trash &amp;<br>Morning Compliance Check Services</div>

  <div class="process">
    <span>Set Out</span><span class="process-arrow"></span>
    <span>Collect</span><span class="process-arrow"></span>
    <span>Check-Up</span><span class="process-arrow"></span>
    <span>Return</span>
  </div>

  <footer class="contact-bar">
    <div class="contact-phone">
      <svg width="32" height="32" viewBox="0 0 24 24" fill="var(--white)"><path d="M6.6 10.8a15.1 15.1 0 0 0 6.6 6.6l2.2-2.2a1 1 0 0 1 1-.25 11.4 11.4 0 0 0 3.6.57 1 1 0 0 1 1 1V20a1 1 0 0 1-1 1A17 17 0 0 1 3 4a1 1 0 0 1 1-1h3.5a1 1 0 0 1 1 1c0 1.25.2 2.45.57 3.57a1 1 0 0 1-.25 1z"/><path d="M15 3a6 6 0 0 1 6 6M15 6a3 3 0 0 1 3 3" stroke="var(--white)" stroke-width="1.6" fill="none" stroke-linecap="round"/></svg>
      <span>555-314-7290</span>
    </div>
    <div class="contact-details">
      <div class="contact-item">
        <svg width="16" height="19" viewBox="0 0 16 20"><path d="M8 0a8 8 0 0 0-8 8c0 6 8 12 8 12s8-6 8-12a8 8 0 0 0-8-8z" fill="var(--white)"/><circle cx="8" cy="8" r="3" fill="var(--navy)"/></svg>
        <span>438 Quarry Ridge Road SUITE<br>Millbrook NJ 08000</span>
      </div>
      <div class="contact-item">
        <svg width="16" height="13" viewBox="0 0 16 13"><rect x=".75" y=".75" width="14.5" height="11.5" fill="none" stroke="var(--white)" stroke-width="1.5"/><path d="M1 1l14 11M15 1L1 12" stroke="var(--white)" stroke-width="1.3"/></svg>
        <span>Marla@lanternway-hauling.example</span>
      </div>
    </div>
  </footer>
</section>

</body>
</html>
```